Stationery design for pet company

We need a designer for stationery designs. The name of our company is Plimarv. We specialise in pet accessories as well as distribution of pet food. We also have a brand under us for our website called Tailwaggroove. We will need a letterhead for Plimarv and another for Tailwaggroove with matching envelopes. We also would like to have a business card design with name, contact details etc with the Plimarv logo on one side of the card. The other side of the business card should have the full logo of Tailwaggroove with our website www.tailwaggroove.example.

Target Market(s)

Stationery for Plimarv is for retail shops and suppliers, therefore should have a more professional feel. Stationery for Tailwaggroove is mainly for customers from the website.

Industry/Entity Type

Business

Requirements
Must have
• Preferably a use of black colour for the business card.
Nice to have
• Professional feel
Should not have
• Childish designs

```html
<!DOCTYPE html>
<html lang="en">
<head>
<meta charset="utf-8">
<title>Plimarv business card</title>
<link rel="stylesheet" href="https://fonts.googleapis.com/css2?family=Quicksand:wght@500;600;700&family=Crimson+Text:ital@1&display=swap">
<style>
  :root {
    --gold: #c8913a;
    --black: #0c0a08;
    --card-grey: #e9f0ef;
    --ink: #141414;
    --paper: #ffffff;
    --brand-blue: #3b35ea;
    --frame-line: #e4ebea;
  }
  html, body {
    margin: 0;
    padding: 0;
    width: 1200px;
    height: 1200px;
    overflow: hidden;
    background: var(--paper);
  }
  .canvas {
    position: relative;
    width: 1200px;
    height: 1200px;
  }

  /* Front side */
  .card-front {
    position: absolute;
    left: 236px;
    top: 128px;
    width: 720px;
    height: 428px;
    background: var(--card-grey);
    border-top: 10px solid var(--gold);
    border-bottom: 12px solid var(--gold);
    box-sizing: border-box;
  }
  .front-header {
    position: relative;
    height: 88px;
    background: var(--black);
  }
  .front-header .brand-name {
    position: absolute;
    right: 44px;
    top: 22px;
    font-family: "Quicksand", sans-serif;
    font-weight: 600;
    font-size: 42px;
    letter-spacing: 3px;
    color: var(--gold);
    text-transform: uppercase;
  }
  .tagline-band {
    position: relative;
    height: 60px;
    background: var(--gold);
  }
  .tagline-band .tagline {
    position: absolute;
    left: 250px;
    top: 6px;
    font-family: "Crimson Text", serif;
    font-style: italic;
    font-size: 38px;
    color: var(--ink);
  }
  .logo-block {
    position: absolute;
    left: 0;
    top: 16px;
    width: 186px;
    height: 132px;
    display: flex;
    flex-direction: column;
    align-items: center;
    justify-content: flex-end;
    gap: 8px;
    padding-bottom: 10px;
    box-sizing: border-box;
    background: var(--black);
  }
  .logo-block .logo-dot {
    width: 52px;
    height: 52px;
    border-radius: 50%;
    background: var(--gold);
  }
  .logo-block .logo-name {
    font-family: "Quicksand", sans-serif;
    font-weight: 600;
    font-size: 30px;
    letter-spacing: 1px;
    color: var(--paper);
  }
  .contact {
    position: absolute;
    left: 14px;
    top: 232px;
    font-family: "Crimson Text", serif;
    font-style: italic;
    font-size: 38px;
    line-height: 54px;
    color: var(--ink);
  }
  .contact p { margin: 0; }

  /* Back side */
  .card-back {
    position: absolute;
    left: 230px;
    top: 594px;
    width: 730px;
    height: 436px;
    background: var(--gold);
    padding: 20px 16px;
    box-sizing: border-box;
  }
  .card-back-inner {
    width: 100%;
    height: 100%;
    background: var(--paper);
    border: 6px solid var(--frame-line);
    box-sizing: border-box;
    display: flex;
    flex-direction: column;
    align-items: center;
    justify-content: center;
    gap: 22px;
  }
  .back-logo-dot {
    width: 150px;
    height: 150px;
    border-radius: 50%;
    background: var(--black);
  }
  .back-brand-name {
    font-family: "Quicksand", sans-serif;
    font-weight: 700;
    font-size: 84px;
    line-height: 1;
    color: var(--brand-blue);
  }
</style>
</head>
<body>
<main class="canvas">

  <section class="card-front" aria-label="Business card front">
    <header class="front-header">
      <span class="brand-name">Plimarv</span>
    </header>
    <div class="tagline-band">
      <span class="tagline">Pet accessories and food</span>
    </div>
    <div class="logo-block">
      <span class="logo-dot"></span>
      <span class="logo-name">Plimarv</span>
    </div>
    <div class="contact">
      <p>box 218 Fernhill Rd</p>
      <p>555-014-782</p>
      <p>www.plimarv.example</p>
    </div>
  </section>

  <section class="card-back" aria-label="Business card back">
    <div class="card-back-inner">
      <span class="back-logo-dot"></span>
      <span class="back-brand-name">Tailwaggroove</span>
    </div>
  </section>

</main>
</body>
</html>
```